Dentistry

Dentist's personal business card. No logo needed. The card shoul deliver the massage of reliability, professionalism, experience.
Please ad the full brief of the project: down the line it says: the winning look should be precise and pristine NO pictures of Teeth, smiles, instruments etc.

The details to be desplaid are:
Dr. Lev Oranbury
Doctor of Dental Surgery
PHD
Web. Www.droranbury.example
Email. Lev@droranbury.example
Tel 07700900318
Surgery address. 27Bfernwick road London SE4 7QX UK
62 Harlow Crescent London EC3V 9PD. Uk

Industry/Entity Type

Massage

Requirements
Should not have
• Logo, teeth, smile any sort of instruments.

```html
<!DOCTYPE html>
<html lang="en">
<head>
<meta charset="utf-8">
<title>Dr. Lev Oranbury — Dental Surgery Business Card</title>
<link rel="stylesheet" href="https://fonts.googleapis.com/css2?family=Montserrat:wght@600;700&family=Open+Sans:wght@600&family=Questrial&display=swap">
<style>
  :root {
    --backdrop: #dcdfd8;
    --card-light: #ececec;
    --card-dark: #343434;
    --ink-dark: #3e3e3e;
    --ink-muted: #8a8a8a;
    --ink-light: #f2f2f2;
    --ink-soft: #cfcfcf;
    --rule: #8c8c8c;
  }
  * { box-sizing: border-box; margin: 0; padding: 0; }
  html, body { width: 1200px; height: 894px; overflow: hidden; }
  body {
    background: var(--backdrop);
    position: relative;
    font-family: "Questrial", sans-serif;
  }

  .card {
    position: absolute;
    box-shadow: 0 6px 18px rgba(0,0,0,0.18);
  }

  /* Appointment card (back) */
  .appointment-card {
    left: 86px; top: 313px;
    width: 622px; height: 314px;
    background: var(--card-light);
  }
  .appointment-card__title {
    position: absolute;
    top: 57px; left: 0; width: 100%;
    text-align: center;
    font-family: "Open Sans", sans-serif;
    font-weight: 600;
    font-size: 15px;
    color: var(--ink-dark);
    letter-spacing: 0.1px;
  }
  .appointment-list {
    position: absolute;
    top: 97px; left: 167px;
    list-style: none;
  }
  .appointment-list__item {
    font-size: 13px;
    color: var(--ink-muted);
    height: 34.5px;
    letter-spacing: 0.3px;
    white-space: nowrap;
  }

  /* Contact card (front) */
  .contact-card {
    left: 418px; top: 520px;
    width: 676px; height: 270px;
    background: var(--card-dark);
    color: var(--ink-light);
  }
  .contact-card__name {
    position: absolute;
    left: 42px; top: 40px;
    font-family: "Montserrat", sans-serif;
    font-weight: 600;
    font-size: 20px;
    letter-spacing: 0.8px;
    text-transform: uppercase;
  }
  .contact-card__role {
    position: absolute;
    left: 43px; top: 66px;
    font-size: 13px;
    color: var(--ink-soft);
    letter-spacing: 0.3px;
  }
  .contact-details {
    position: absolute;
    left: 0; bottom: 18px;
    width: 100%; height: 66px;
    display: flex;
  }
  .contact-details__item {
    display: flex;
    flex-direction: column;
    justify-content: center;
    font-size: 12px;
    line-height: 15px;
    letter-spacing: 0.3px;
    white-space: nowrap;
  }
  .contact-details__item--phone { width: 226px; padding-left: 42px; }
  .contact-details__item--email { width: 206px; padding-left: 22px; border-left: 1px solid var(--rule); }
  .contact-details__item--address { flex: 1; padding-left: 22px; border-left: 1px solid var(--rule); }
  .contact-details__label {
    font-family: "Montserrat", sans-serif;
    font-weight: 700;
    font-size: 11px;
    margin-right: 4px;
  }
</style>
</head>
<body>

  <section class="card appointment-card" aria-label="Appointment card">
    <h2 class="appointment-card__title">Your Appointments</h2>
    <ol class="appointment-list">
      <li class="appointment-list__item">1.&nbsp; ___am/pm ______________ ___/___/___</li>
      <li class="appointment-list__item">2.&nbsp; ___am/pm ______________ ___/___/___</li>
      <li class="appointment-list__item">3.&nbsp; ___am/pm ______________ ___/___/___</li>
      <li class="appointment-list__item">4.&nbsp; ___am/pm ______________ ___/___/___</li>
      <li class="appointment-list__item">5.&nbsp; ___am/pm ______________ ___/___/___</li>
    </ol>
  </section>

  <section class="card contact-card" aria-label="Contact card">
    <h1 class="contact-card__name">Dr. Lev Oranbury</h1>
    <p class="contact-card__role">Doctor of Dental Surgery · PhD</p>
    <div class="contact-details">
      <div class="contact-details__item contact-details__item--phone">
        <p><span class="contact-details__label">T:</span>07700900318</p>
        <p><span class="contact-details__label">W:</span>Www.droranbury.example</p>
      </div>
      <div class="contact-details__item contact-details__item--email">
        <p><span class="contact-details__label">E:</span>Lev@droranbury.example</p>
      </div>
      <div class="contact-details__item contact-details__item--address">
        <p>27Bfernwick road</p>
        <p>London SE4 7QX UK</p>
        <p>62 Harlow Crescent</p>
        <p>London EC3V 9PD UK</p>
      </div>
    </div>
  </section>

</body>
</html>
```